Lantern Advisory
Letterhead design for Marketing Company
Bright & Fun-filled
Nadia Corvane
Inspiration Director
No address needed, please disregard
lanternadvise@mailbrook.net
www.lanternadvisory.ca
Certified QTPR Practitioner B.A. Linguistics
Ask about any of the following services: Corporate workshops Diversity Training Marketing Analysis Career Counseling Entrepreneur Motivation Package QTPR Personality Testing Accent Reduction

```html
<!DOCTYPE html>
<html lang="en">
<head>
<meta charset="utf-8">
<title>Lantern Advisory — Business Card</title>
<link rel="stylesheet" href="https://fonts.googleapis.com/css2?family=Arimo:wght@400;700&display=swap">
<style>
  :root {
    --bg: #e9e7e3;
    --card-white: #ffffff;
    --card-black: #0c0c0c;
    --brand-yellow: #f7c600;
    --ink: #1a1a1a;
    --ink-soft: #4a4a4a;
    --stripe-grey: #b9b9b9;
    --on-dark: #f2f2f2;
  }
  * { box-sizing: border-box; margin: 0; padding: 0; }
  html, body {
    width: 1200px; height: 901px; overflow: hidden;
    background: var(--bg);
    font-family: "Arimo", Arial, sans-serif;
  }
  .canvas {
    position: relative; width: 1200px; height: 901px;
  }
  .card {
    position: absolute; left: 250px;
    width: 700px; height: 400px;
    border-radius: 22px; overflow: hidden;
    box-shadow: 0 6px 18px rgba(0,0,0,.18);
  }
  .card-back { top: 34px; background: var(--card-black); color: var(--on-dark); }
  .card-front { top: 467px; background: var(--card-white); color: var(--ink); }

  /* back */
  .back-brand {
    position: absolute; left: 0; right: 0; top: 78px;
    display: flex; align-items: center; justify-content: center; gap: 12px;
  }
  .brand-dot {
    width: 18px; height: 18px; border-radius: 50%;
    background: var(--brand-yellow);
  }
  .back-brand .brand-name {
    font-weight: 700; font-size: 34px; color: var(--on-dark); letter-spacing: .5px;
  }
  .service-list {
    position: absolute; left: 0; right: 0; top: 160px;
    list-style: none; text-align: center;
    font-size: 17px; line-height: 25px; color: var(--on-dark);
  }

  /* front */
  .front-swoosh { position: absolute; inset: 0; }
  .front-brand {
    position: absolute; left: 62px; top: 62px;
    display: flex; align-items: center; gap: 12px;
  }
  .front-brand .brand-name {
    font-weight: 700; font-size: 38px; color: var(--ink); letter-spacing: .5px;
  }
  .person { position: absolute; left: 66px; top: 168px; }
  .person-name { font-weight: 700; font-size: 25px; color: var(--brand-yellow); }
  .person-title { font-size: 16px; color: var(--ink-soft); margin-top: 4px; }
  .contact-list {
    position: absolute; left: 66px; top: 268px;
    list-style: none; font-size: 16px; line-height: 26px; color: var(--ink);
  }
  .contact-list li { display: flex; align-items: center; gap: 10px; }
  .contact-icon { width: 14px; height: 14px; flex: none; }
</style>
</head>
<body>
<main class="canvas">

  <section class="card card-back" aria-label="Card back">
    <div class="back-brand">
      <span class="brand-dot"></span>
      <span class="brand-name">Lantern Advisory</span>
    </div>
    <ul class="service-list">
      <li>Corporate workshops</li>
      <li>Diversity Training</li>
      <li>Marketing Analysis</li>
      <li>Career Counseling</li>
      <li>Entrepreneur Motivation Package</li>
      <li>QTPR Personality Testing</li>
      <li>Accent Reduction</li>
    </ul>
  </section>

  <section class="card card-front" aria-label="Card front">
    <svg class="front-swoosh" viewBox="0 0 700 400" preserveAspectRatio="none" aria-hidden="true">
      <path d="M610 0 Q570 250 430 400 L700 400 L700 0 Z" fill="var(--brand-yellow)"/>
      <path d="M700 160 Q575 258 512 400 L700 400 Z" fill="var(--stripe-grey)"/>
      <path d="M700 176 Q588 268 528 400 L700 400 Z" fill="var(--card-black)"/>
    </svg>

    <div class="front-brand">
      <span class="brand-dot"></span>
      <span class="brand-name">Lantern Advisory</span>
    </div>

    <div class="person">
      <p class="person-name">Nadia Corvane</p>
      <p class="person-title">Inspiration Director</p>
    </div>

    <ul class="contact-list">
      <li>
        <svg class="contact-icon" viewBox="0 0 14 14" aria-hidden="true"><rect x="3" y="0.5" width="8" height="13" rx="1.5" fill="var(--brand-yellow)"/><rect x="4.5" y="2" width="5" height="8" fill="#fff"/></svg>
        780-555-0142
      </li>
      <li>
        <svg class="contact-icon" viewBox="0 0 14 14" aria-hidden="true"><rect x="0.5" y="2.5" width="13" height="9" rx="1" fill="var(--brand-yellow)"/><path d="M1 3 L7 8 L13 3" stroke="#fff" stroke-width="1.2" fill="none"/></svg>
        lanternadvise@mailbrook.net
      </li>
      <li>
        <svg class="contact-icon" viewBox="0 0 14 14" aria-hidden="true"><circle cx="7" cy="7" r="6" fill="var(--brand-yellow)"/><path d="M1 7 H13 M7 1 Q3 7 7 13 M7 1 Q11 7 7 13" stroke="#fff" stroke-width="1" fill="none"/></svg>
        www.lanternadvisory.ca
      </li>
    </ul>
  </section>

</main>
</body>
</html>
```